Website design for dressage horse training business

Looking to develop a new website design for a dressage horse training website. We want to change from a single landing page to one with multiple pages.
You are free to use your creativity to design the main landing page. This is the only page you need to design at this point. I would encourage looking at other Dressage Training websites to get a feel for what is typically on them. A few websites are listed below although I think the design of them could be better.
Notes:
- Menu to include: Home, Services, News Room, Blog, About Us, Contact,
- FAQ section on main page
- Logo to remain the same - the logo attached is not the correct color so change to match existing color.
- Change 'Sponsors' to 'Partnerships' on main page
Here is the link to the current site:
https://lindenridgestables.com/
Example sites
https://www.crestwoodsporthorsesco.com/
https://corinnalavelledressage.com/
Target Market(s)
Older women with disposable income
Number of Pages Required
1 page
Look and feel
Each slider illustrates characteristics of the customer's brand and the style your logo design should communicate.

```html
<!DOCTYPE html>
<html lang="en">
<head>
<meta charset="utf-8">
<title>Linden Ridge Stables</title>
<link href="https://fonts.googleapis.com/css2?family=Poppins:wght@300;400;500&family=Roboto:wght@400;500&display=swap" rel="stylesheet">
<style>
:root{
  --gold:#c39a6e;
  --ink:#1b1b1b;
  --muted:#4a4a4a;
  --dark:#2a2520;
  --line:#d9d9d9;
  --bg:#f4f4f4;
}
*{box-sizing:border-box;margin:0;padding:0}
html,body{width:1200px;height:3788px;overflow:hidden;background:var(--bg);font-family:'Poppins',sans-serif;color:var(--ink)}
.page{position:absolute;left:150px;top:43px;width:900px;background:#fff;box-shadow:0 10px 40px rgba(0,0,0,.08)}
h1,h2,h3,h4{font-family:'Roboto',sans-serif;font-weight:500}
.btn{display:inline-block;background:var(--gold);color:#fff;font-size:9px;letter-spacing:.5px;padding:6px 12px;text-transform:uppercase}
.btn-outline{background:transparent;border:2px solid #fff;font-size:11px}
.rule{display:flex;gap:6px;margin:10px 0 16px}
.rule span{display:block;height:3px;background:var(--gold)}
.rule span:first-child{width:70px}.rule span:last-child{width:22px}
.rule.light span{background:#fff}
.rule.center{justify-content:center}
/* header */
.site-header{height:54px;display:flex;align-items:center;padding:0 44px 0 56px;justify-content:space-between}
.brand{font-family:'Poppins',sans-serif;font-weight:400;color:var(--gold);font-size:19px;letter-spacing:1px;display:flex;align-items:center;gap:6px}
.brand i{display:block;width:8px;height:8px;border-radius:50%;background:var(--gold)}
.nav{display:flex;gap:14px;font-size:10px;margin-left:140px}
.nav a{color:var(--ink);text-decoration:none}
.nav a.active{border-bottom:2px solid var(--gold);padding-bottom:3px}
.search{border:1px solid var(--gold);font-size:10px;padding:4px 8px;width:70px;display:flex;justify-content:space-between}
/* hero */
.hero{position:relative;height:448px;background:linear-gradient(160deg,#6d4d22 0%,#3a2a14 40%,#1a140c 70%,#2b2a27 100%);color:#fff}
.hero-photo-horse{position:absolute;right:120px;top:30px;width:190px;height:418px;border-radius:90px 90px 0 0;background:linear-gradient(180deg,#c9c4b8,#8f8a80)}
.hero-copy{position:absolute;left:53px;top:172px}
.hero h1{font-size:35px;line-height:38px}
.hero p{font-size:26px;font-weight:300;margin-top:8px}
.hero .rule span{background:#fff;height:3px}
.hero .rule span:first-child{width:160px}.hero .rule span:last-child{width:30px}
.hero .actions{display:flex;gap:10px;margin-top:14px}
.hero .btn{font-size:11px;padding:7px 18px}
/* about */
.about{height:506px;position:relative}
.about-photo{position:absolute;left:128px;top:68px;width:244px;height:370px;border-radius:48% 52% 40% 60%/40% 30% 70% 60%;background:linear-gradient(160deg,#9a7a58,#5a4a3a)}
.about-copy{position:absolute;left:445px;top:122px;width:360px}
.about h2{font-size:26px}
.about p{font-size:11.5px;line-height:19px;color:var(--muted)}
.about .btn{margin-top:18px}
/* dark bands */
.band{position:relative;background:linear-gradient(90deg,#3e3328,#241e18 50%,#1c1a18);color:#fff;text-align:center}
.band h2{font-size:26px;padding-top:40px}
.cards{position:absolute;left:154px;display:flex;gap:60px}
.card{width:265px;height:300px;background:#f4f4f4;border:3px solid var(--gold);color:var(--ink);padding:30px 36px 0;text-align:center}
.card h3{font-size:19px}
.card .rule{margin:10px 0 18px}
.card .rule span:first-child{width:40px}.card .rule span:last-child{width:12px}
.card p{font-size:10px;line-height:16.5px;color:var(--muted)}
.card .btn{margin-top:16px;font-size:6px;padding:4px 10px}
.training{height:486px}.training .cards{top:130px}
.partners{height:488px}.partners .cards{top:130px}.partners .card{padding-top:14px}
.badge{width:104px;height:36px;margin:0 auto 8px;border-radius:50%;background:#8a2f23}
.badge.square{width:38px;height:38px;border-radius:4px;background:#5a5a5a}
/* sale */
.sale{height:502px;position:relative}
.sale-photo{position:absolute;left:106px;top:86px;width:293px;height:330px;background:linear-gradient(150deg,#6e5324,#a89e8a 55%,#3a2e1c)}
.sale-copy{position:absolute;left:443px;top:114px;width:360px}
.sale h4{font-size:17px}
.sale h2{font-size:26px}
.sale p{font-size:11.5px;line-height:19px;color:var(--muted)}
.sale .btn{margin-top:18px}
/* faq */
.faq{height:564px;position:relative}
.faq-copy{position:absolute;left:72px;top:127px;width:386px}
.faq h4{font-size:14px;font-weight:400}
.faq h2{font-size:25px}
.faq ul{list-style:none}
.faq li{display:flex;justify-content:space-between;font-size:11px;padding:12px 6px 12px 4px;border-bottom:1px solid var(--line);color:var(--muted)}
.faq-photo{position:absolute;left:538px;top:110px;width:293px;height:345px;background:linear-gradient(135deg,#5a6e46,#8a7a5a 50%,#4a6a8a)}
/* contact */
.contact{height:398px;position:relative;background:linear-gradient(90deg,#2a241d,#3b3026 60%,#1e1b17);color:#fff}
.contact-info{position:absolute;left:107px;top:40px}
.contact-info h2{font-size:28px}
.contact-info h4{font-size:17px;margin-top:24px}
.contact-info p{font-size:9px;line-height:14px}
.contact-info a{color:#fff;font-size:9px;display:block;text-decoration:underline}
.contact-form{position:absolute;left:369px;top:118px;width:430px;display:grid;grid-template-columns:1fr 1fr;column-gap:44px;row-gap:18px;font-size:9px}
.field{border-bottom:1px solid #bbb;padding-bottom:6px}
.field.wide{grid-column:1/3;height:74px}
.contact-form .btn{width:84px;text-align:center;font-size:10px;padding:7px 0}
/* footer */
.site-footer{height:228px;position:relative}
.site-footer .brand{position:absolute;left:96px;top:72px}
.footer-blurb{position:absolute;left:60px;top:118px;width:190px;font-size:8px;line-height:11px;text-align:center}
.fcol{position:absolute;top:54px}
.fcol h5{font-size:13px;font-weight:500;margin-bottom:10px}
.fcol li{list-style:none;font-size:9px;line-height:16px}
.fcol .rule{margin:4px 0 10px}
.icons{display:flex;gap:12px;margin-top:4px}
.copyright{height:28px;background:#111;color:#ddd;font-size:9px;text-align:center;line-height:28px}
</style>
</head>
<body>
<div class="page">
  <header class="site-header">
    <div class="brand"><i></i>LINDEN RIDGE</div>
    <nav class="nav"><a class="active" href="#">Home</a><a href="#">Services</a><a href="#">News Room</a><a href="#">Blog</a><a href="#">About Us</a><a href="#">Contact</a></nav>
    <div class="search"><span>Search</span>
      <svg width="10" height="10" viewBox="0 0 10 10"><circle cx="4" cy="4" r="3" fill="none" stroke="#1b1b1b"/><line x1="6.2" y1="6.2" x2="9" y2="9" stroke="#1b1b1b"/></svg></div>
  </header>

  <section class="hero" role="img" aria-label="Grey horse in a halter against autumn foliage">
    <div class="hero-photo-horse"></div>
    <div class="hero-copy">
      <h1>The Linden Valley's Premier<br>dressage and sport horse training</h1>
      <div class="rule"><span></span><span></span></div>
      <p>Located outside Linden Falls</p>
      <div class="actions"><span class="btn">Services</span><span class="btn btn-outline">Contact Us</span></div>
    </div>
  </section>

  <section class="about">
    <div class="about-photo" role="img" aria-label="Rider jumping a bay horse"></div>
    <div class="about-copy">
      <h2>ABOUT US</h2>
      <div class="rule"><span></span><span></span></div>
      <p>International-level rider and trainer, Helena Draves began her riding career at a young age. She went up through the ranks of a youth riding club with an emphasis and focus in eventing. During college, Helena worked for a small breeder starting young horses. Helena loves starting young horses including starting and guiding them in a correct and quiet way to help them flourish. Her training focuses on gymnastic training incorporating ground work/lunging/long lining, jumping, cavelletti and regular hacking and trail riding.</p>
      <span class="btn">Learn More ›</span>
    </div>
  </section>

  <section class="band training" role="img" aria-label="Rider on horseback in an arena">
    <h2>Training &amp; Lessons</h2>
    <div class="rule light center"><span></span><span></span></div>
    <div class="cards">
      <div class="card"><h3>Lessons</h3><div class="rule center"><span></span><span></span></div>
        <p>Lessons are available for all ages of riders. Helena thoroughly enjoys working with accomplished riders looking to succeed in the show ring, as well as riders just wanting to learn what dressage is about. Come join our incredible and encouraging team! Come join our incredible and encouraging team!</p><span class="btn">Learn More</span></div>
      <div class="card"><h3>Training</h3><div class="rule center"><span></span><span></span></div>
        <p>Linden Ridge offers both full and half time training options with Helena Draves. There is much flexibility with both rides and/or lessons weekly in the training packages that can be customized to fit both the horse and the rider's needs. Generally, full training provides 3-4 "working days" of riding, and 1-2</p><span class="btn">Learn More</span></div>
    </div>
  </section>

  <section class="sale">
    <div class="sale-photo" role="img" aria-label="Grey horse with bridle in front of autumn trees"></div>
    <div class="sale-copy">
      <h4>For Sale</h4>
      <h2>Silver Meridian</h2>
      <div class="rule"><span></span><span></span></div>
      <p>Silver Meridian, "Milo," (Solstice x Noble Pilot) is a 2012, 16hh imported Hanoverian. Milo is an incredibly quiet and kind horse. He is ridden by both an amatuer and child rider. He loves to hack and is very quiet alone and with a group of horses. He has shown through first level with scores into the 70's at both training and first level. Milo is currently solidly schooling all of second level, as well as half passes and flying changes from third level. Milo has 3 very easy to ride</p>
      <span class="btn">Learn More ›</span>
    </div>
  </section>

  <section class="band partners" role="img" aria-label="Rider on horseback in an arena">
    <h2 style="letter-spacing:2px">Partnerships</h2>
    <div class="rule light center"><span></span><span></span></div>
    <div class="cards">
      <div class="card"><div class="badge"></div><h3>Fieldcrest Saddlery</h3><div class="rule center"><span></span><span></span></div>
        <p>Fieldcrest Saddlery is constantly designing and researching saddles and riders to find the right blend of design and craftsmanship to fit today's demands. Every saddle's detail is carefully checked to be sure the workmanship and quality is there. All saddles are anatomically</p><span class="btn">Learn More</span></div>
      <div class="card"><div class="badge square"></div><h3>Marlow's Saddlery</h3><div class="rule center"><span></span><span></span></div>
        <p>My goal is to provide the best possible fit for both horse and rider whether it is a saddle you already own, one you have on trial, or one that I carry. Being a Qualified Saddle Fitter by the Guild of Saddle Fitters allows me to work with all saddle types and brands. In</p><span class="btn">Learn More</span></div>
    </div>
  </section>

  <section class="faq">
    <div class="faq-copy">
      <h4>What You Need To Know</h4>
      <h2>Frequently Asked Questions</h2>
      <div class="rule"><span></span><span></span></div>
      <ul>
        <li>What do you need to register your company<span>+</span></li>
        <li>Are there any hidden costs<span>+</span></li>
        <li>How many shares does a company need<span>+</span></li>
        <li>What happened after your company is registered<span>+</span></li>
        <li>how can I receive my cashback offer<span>+</span></li>
        <li>Can I set up a company on my own<span>+</span></li>
      </ul>
    </div>
    <div class="faq-photo" role="img" aria-label="Woman standing beside a bay horse outdoors"></div>
  </section>

  <section class="contact" role="img" aria-label="Horses in a dark paddock">
    <div class="contact-info">
      <h2>Get In Touch</h2>
      <div class="rule"><span></span><span></span></div>
      <h4 style="margin-top:10px">Find Us</h4>
      <p>418 Orchard Lane, Linden Falls 00418<br>Linden Valley</p>
      <h4>Get In Touch</h4>
      <p>hello@lindenridgestables.com<br>+1 (555) 555-0142</p>
      <h4>Legal Stuff</h4>
      <a href="#">Privacy &amp; Policy</a><a href="#">Terms &amp; Conditions</a>
    </div>
    <form class="contact-form">
      <div class="field">Name</div><div class="field">Email</div>
      <div class="field">Phone</div><div class="field" style="display:flex;justify-content:space-between">Country<span>⌄</span></div>
      <div class="field wide">Enter You Message</div>
      <span class="btn">Submit ›</span>
    </form>
  </section>

  <footer class="site-footer">
    <div class="brand"><i></i>LINDEN RIDGE</div>
    <p class="footer-blurb">Lorem ipsum dolor sit amet, consetetur sadipscing elitr, sed diam nonumy eirmod tempor invidunt ut labore et dolore magna</p>
    <div class="fcol" style="left:329px"><h5>USEFULL LINKS</h5><div class="rule"><span style="width:40px"></span><span style="width:12px"></span></div>
      <ul><li>Home</li><li>Services</li><li>News Room</li><li>Blog</li><li>About Us</li><li>Contact</li></ul></div>
    <div class="fcol" style="left:513px"><h5>CONTACT US</h5><div class="rule"><span style="width:40px"></span><span style="width:12px"></span></div>
      <ul><li>⌖ 418 Orchard Lane, Linden Falls</li><li>✆ +1 (555) 555-0142</li><li>✉ hello@lindenridgestables.com</li></ul></div>
    <div class="fcol" style="left:719px"><h5>SOCIAL LINKS</h5><div class="rule"><span style="width:40px"></span><span style="width:12px"></span></div>
      <div class="icons"><svg width="14" height="14"><circle cx="7" cy="7" r="6" fill="#1b1b1b"/></svg><svg width="14" height="14"><circle cx="7" cy="7" r="6" fill="#1b1b1b"/></svg><svg width="14" height="14"><rect x="1" y="1" width="12" height="12" rx="3" fill="#1b1b1b"/></svg></div></div>
  </footer>
  <div class="copyright">© 2021 Linden Ridge Stables. All Rights Reserved.</div>
</div>
</body>
</html>
```